New Business Card Needed

I need a new business card for Meridale Kitchen & Bath.
Logo is attached as well a my photo. Note: Make the logo Navy Blue.
Here is the text:
Gregory Tenwick
GC/Owner
Charlotte NC
704-555-0139
gregory@meridaleHVX.com
www.meridaleHVX.com
Tag line on card: BEAUTY | FUNCTION | ON TIME | ON BUDGET
Trim size: 2.56" X 2.56"
This is where we aim to cut the cards.
Safe area: 2.4" X 2.4"
Make sure any important aspects of your design such as text and logos are inside of the safe area, otherwise they may be cut off.
Bleed area: 2.71 X 2.71
Make sure that your background extends to fill the bleed to avoid your Business Cards having white edges when trimmed.
On the back side. Use photo of kitchen attached.

```html
<!DOCTYPE html>
<html lang="en">
<head>
<meta charset="utf-8">
<title>Meridale Kitchen &amp; Bath – Business Card</title>
<link href="https://fonts.googleapis.com/css2?family=Montserrat:wght@400;600&display=swap" rel="stylesheet">
<style>
  :root {
    --canvas: #ffffff;
    --sage: #4b5f49;
    --sage-ink: #263425;
    --forest: #1c291c;
    --forest-deep: #0b150c;
    --mist: #c9d1c5;
    --guide-trim: #e23b3b;
    --guide-bleed: #3a3fc4;
    --guide-safe: #3f9a4a;
  }
  * { box-sizing: border-box; margin: 0; padding: 0; }
  html, body {
    width: 1200px; height: 625px; overflow: hidden;
    background: var(--canvas);
    font-family: "Montserrat", Arial, sans-serif;
  }
  .sheet { position: relative; width: 1200px; height: 625px; }

  .card {
    position: absolute; top: 47px; width: 522px; height: 522px;
    overflow: hidden; border: 1px solid var(--guide-trim);
  }
  .card--front { left: 43px; background: var(--forest); }
  .card--back { left: 634px; }

  .front__info {
    position: absolute; left: 0; top: 0; width: 100%; height: 265px;
    background: var(--sage);
  }
  .contact {
    position: absolute; left: 58px; top: 52px; list-style: none;
    color: var(--sage-ink); font-size: 20.5px; font-weight: 400;
    line-height: 32.1px; letter-spacing: 0.3px;
  }
  .contact__web { font-weight: 600; }

  .front__brand {
    position: absolute; left: 0; top: 265px; width: 293px; height: 257px;
    background: var(--forest);
  }
  .brand-name {
    position: absolute; left: 58px; top: 54px;
    color: var(--mist); font-size: 22px; font-weight: 400;
    line-height: 28px;
  }
  .tagline {
    position: absolute; left: 58px; top: 147px;
    color: var(--mist); font-size: 16px; font-weight: 400;
    line-height: 19.5px; letter-spacing: 0.3px; white-space: nowrap;
  }

  .front__portrait-bg {
    position: absolute; left: 292px; top: 265px; width: 230px; height: 257px;
    background: var(--forest-deep);
  }
  .portrait {
    position: absolute; left: 292px; top: 288px; width: 215px; height: 212px;
    background: radial-gradient(ellipse at 50% 40%, #9a6f55 0%, #5a4234 40%, #1f2530 75%, #0b150c 100%);
  }

  .kitchen-photo {
    position: absolute; inset: 0;
    background: linear-gradient(180deg, #e9e6e0 0%, #f3f1ee 35%, #cfae86 58%, #eeeeec 62%, #e2e2e0 80%, #c79d6e 92%, #3a3a38 100%);
  }

  .guide { position: absolute; border: 1px solid; pointer-events: none; }
  .guide--bleed { left: 14px; top: 14px; width: 494px; height: 494px; border-color: var(--guide-bleed); }
  .guide--safe { left: 29px; top: 30px; width: 463px; height: 462px; border-color: var(--guide-safe); }
</style>
</head>
<body>
<main class="sheet">
  <section class="card card--front" aria-label="Card front">
    <div class="front__info">
      <ul class="contact">
        <li>Gregory Tenwick</li>
        <li>GC/Owner</li>
        <li>Charlotte NC</li>
        <li>704-555-0139</li>
        <li>gregory@meridaleHVX.com</li>
        <li class="contact__web">www.meridaleHVX.com</li>
      </ul>
    </div>
    <div class="front__brand">
      <p class="brand-name">Meridale<br>Kitchen &amp; Bath</p>
      <p class="tagline">BEAUTY | FUNCTION |<br>ON TIME | ON<br>BUDGET</p>
    </div>
    <div class="front__portrait-bg"></div>
    <div class="portrait" role="img" aria-label="Portrait photo of the owner"></div>
    <div class="guide guide--bleed"></div>
    <div class="guide guide--safe"></div>
  </section>

  <section class="card card--back" aria-label="Card back">
    <div class="kitchen-photo" role="img" aria-label="Photo of a bright kitchen with open wooden shelves, white tile and a dining table with flowers"></div>
    <div class="guide guide--safe"></div>
  </section>
</main>
</body>
</html>
```